Flyer for family counseling

For my family counseling I'm looking for a design for flyers. Important is not only the appearance of the flyer, but also the content design. All important contents can be found on my website: www.helga-brandtner.at The following items should NOT appear on the flyer: - constellation work - bereavement and palliative work My logo should definitely be on the flyer. Source files are available.

Target Market(s)

Families, individuals, children, couples in need of psychological support.

Colors

Designer to choose colors to be used in the design.

Requirements
Must have
• My logo - source files available Website and contact data Recognition value from website to flyer and vice versa
Should not have
• Mention of the constellation work and mourning and palliative work not desired.

```html
<!DOCTYPE html>
<html lang="de">
<head>
<meta charset="utf-8">
<title>Familienberatung Flyer</title>
<link href="https://fonts.googleapis.com/css2?family=Open+Sans:wght@300;400;600&display=swap" rel="stylesheet">
<style>
  :root {
    --teal: #33b8a7;
    --teal-deep: #24a596;
    --blue: #1c78c0;
    --blue-text: #1f6db3;
    --body-grey: #555a5e;
    --panel-tint: #eef8f9;
    --white: #ffffff;
  }
  * { margin: 0; padding: 0; box-sizing: border-box; }
  html, body { width: 917px; height: 1200px; overflow: hidden; background: #e9e9e9; }
  .flyer {
    position: relative; width: 917px; height: 1200px; overflow: hidden;
    font-family: "Open Sans", Arial, sans-serif; background: var(--white);
  }
  .flyer-shapes { position: absolute; inset: 0; }
  .intro {
    position: absolute; left: 21px; top: 440px; width: 328px;
    color: var(--white); text-align: center;
  }
  .intro-title { font-size: 20px; font-weight: 400; line-height: 28px; }
  .intro-text {
    margin: 34px 20px 0 30px; font-size: 15.5px; font-weight: 300; line-height: 24px;
    text-align: justify; hyphens: manual;
  }
  .brand {
    position: absolute; left: 351px; top: 470px; width: 566px; text-align: center;
    color: var(--blue-text); font-weight: 400;
  }
  .brand-mark {
    width: 70px; height: 70px; border-radius: 50%; border: 6px solid var(--blue-text);
    margin: 0 auto 26px;
  }
  .brand-name { font-size: 22px; letter-spacing: 2px; text-transform: uppercase; line-height: 28px; }
  .brand-line { font-size: 13px; letter-spacing: 6px; text-transform: uppercase; line-height: 22px; }
  .message {
    position: absolute; left: 380px; top: 680px; width: 510px; text-align: center;
    color: var(--blue-text); font-size: 20px; line-height: 29px; font-weight: 400;
  }
  .message-lead { margin-bottom: 36px; }
  .details {
    position: absolute; left: 482px; top: 840px; width: 415px;
    color: var(--body-grey); font-size: 15px; font-weight: 300; line-height: 23px; text-align: justify;
  }
  .details p + p { margin-top: 23px; }
  .contact {
    position: absolute; left: 0; top: 1150px; width: 917px; height: 30px;
    display: flex; align-items: center; justify-content: space-between; padding: 0 36px 0 28px;
    color: var(--white); font-size: 17px; font-weight: 300;
  }
  .contact-item { display: flex; align-items: center; gap: 10px; }
  .contact-item svg { width: 20px; height: 20px; }
</style>
</head>
<body>
<div class="flyer">
  <svg class="flyer-shapes" width="917" height="1200" viewBox="0 0 917 1200" aria-hidden="true">
    <defs>
      <linearGradient id="photoTone" x1="0" y1="0" x2="1" y2="1">
        <stop offset="0" stop-color="#efe3d2"/>
        <stop offset="0.45" stop-color="#b9a98c"/>
        <stop offset="0.7" stop-color="#7d8a5a"/>
        <stop offset="1" stop-color="#c9a7a1"/>
      </linearGradient>
      <linearGradient id="panelTone" x1="0" y1="0" x2="1" y2="1">
        <stop offset="0" stop-color="#ffffff"/>
        <stop offset="1" stop-color="#eef8f9"/>
      </linearGradient>
      <radialGradient id="roundPhotoTone" cx="0.5" cy="0.45" r="0.6">
        <stop offset="0" stop-color="#e9d6b8"/>
        <stop offset="0.6" stop-color="#a8b773"/>
        <stop offset="1" stop-color="#c98f6c"/>
      </radialGradient>
    </defs>
    <rect class="teal-field" x="0" y="330" width="917" height="760" fill="var(--teal-deep)"/>
    <rect class="column-field" x="21" y="400" width="330" height="680" fill="var(--teal)"/>
    <rect class="column-margin" x="0" y="400" width="21" height="640" fill="#f2f7f7"/>
    <path class="right-panel" d="M351,436 C500,400 700,430 917,540 V1090 H351 Z" fill="url(#panelTone)"/>
    <path class="panel-swoosh" d="M700,460 C820,520 880,640 900,760 C870,650 800,540 700,460 Z" fill="#ffffff" opacity="0.8"/>
    <g role="img" aria-label="Foto: Beraterin im Gespräch mit einer Familie auf Sesseln, Pflanzen im Hintergrund">
      <path class="hero-photo" d="M0,0 H917 V362 C700,420 420,430 0,352 Z" fill="url(#photoTone)"/>
    </g>
    <path class="hero-edge" d="M0,352 C420,430 700,420 917,362 V380 C700,440 420,448 0,372 Z" fill="#ffffff" opacity="0.35"/>
    <path class="bottom-band" d="M0,1010 C260,1060 520,1085 917,1072 V1200 H0 Z" fill="var(--blue)"/>
    <circle class="round-photo-frame" cx="172" cy="1000" r="126" fill="#d7eff0"/>
    <g role="img" aria-label="Foto: Kind spielt mit Beraterin und Bausteinen am Tisch">
      <circle class="round-photo" cx="172" cy="1000" r="113" fill="url(#roundPhotoTone)"/>
    </g>
  </svg>

  <section class="intro">
    <h2 class="intro-title">Gemeinsam leben<br>Was ist eine Familienberatung<br>und wie läuft sie ab?</h2>
    <p class="intro-text">Nach dem zuerst gemeinsam durch die Familie definierten Ziel wird der Fokus auf die Stärken und Ressour&shy;cen der Familie gelegt, da ich als Beraterin davon ausgehe, dass die Kompetenz zur Lösung des Problems immer in der Familie selbst liegt und lediglich professio&shy;neller, wertschätzender Begleitung bedarf.</p>
  </section>

  <div class="brand">
    <div class="brand-mark"></div>
    <div class="brand-name">Helga Brandtner</div>
    <div class="brand-line">Familienberatung Donaufeld</div>
  </div>

  <section class="message">
    <p class="message-lead">Eigenmächtig aus der Krise</p>
    <p>Reicht es Ihnen?<br>Ist ein Punkt erreicht, an dem nichts mehr geht?<br>Ist die Zeit reif für Veränderung?</p>
  </section>

  <section class="details">
    <p>Es gibt Wege aus der Sackgasse. Viele! Genug Ressourcen – sie müssen nur frei gelegt werden.</p>
    <p>Für den ganz persönlichen Weg zur Selbstbestimmung. Ist er einmal betreten, wird die persönliche Entwicklung ein wunder&shy;volles Abenteuer.</p>
  </section>

  <footer class="contact">
    <span class="contact-item">
      <svg viewBox="0 0 20 20" aria-hidden="true"><path d="M10 1a6.5 6.5 0 0 0-6.5 6.5C3.5 12.5 10 19 10 19s6.5-6.5 6.5-11.5A6.5 6.5 0 0 0 10 1zm0 9a2.5 2.5 0 1 1 0-5 2.5 2.5 0 0 1 0 5z" fill="#fff"/></svg>
      Lindenweg 14/3, 1220 Wien
    </span>
    <span class="contact-item">
      <svg viewBox="0 0 20 20" aria-hidden="true"><circle cx="10" cy="10" r="8.5" fill="none" stroke="#fff" stroke-width="1.4"/><path d="M7 5.5l1.6 2.3-1 1.1c.6 1.3 1.6 2.3 2.6 2.9l1.1-1 2.3 1.5-.8 1.7c-3.3-.4-6.2-3.5-6.6-6.8z" fill="#fff"/></svg>
      +43 660 418 27 95
    </span>
    <span class="contact-item">
      <svg viewBox="0 0 20 20" aria-hidden="true"><g fill="none" stroke="#fff" stroke-width="1.2"><circle cx="10" cy="10" r="8"/><ellipse cx="10" cy="10" rx="3.5" ry="8"/><path d="M2 10h16M3.5 6h13M3.5 14h13"/></g></svg>
      www.helga-brandtner.at
    </span>
  </footer>
</div>
</body>
</html>
```